New web page design for our brand Casa Olmera

We have changed our logo and the image of our products, so we would like to redesign ,our web page as well according to the new design.
Our cosmetic products are based in nature and tradition, like they used to be prepared in the old pharmacies.
Our actual web is www.casaolmera.es, so we need similar estructure but completely different design.

Industry/Entity Type

Cosmetics

Number of Pages Required

5+ page

Requirements
Must have
• References to natural ingredients and also to old pharmacys or apothecaries.
Nice to have
• Nature images or old botanics drawings
• I would like to have a cover page with just an image saying welcome to Casa Olmera's world

```html
<!DOCTYPE html>
<html lang="es">
<head>
<meta charset="utf-8">
<title>Casa Olmera – Cosmética natural</title>
<link href="https://fonts.googleapis.com/css2?family=Lobster&family=Open+Sans:wght@400;600;700&display=swap" rel="stylesheet">
<style>
:root{
  --wine:#7d1416;
  --wine-dark:#5e0d0f;
  --ink:#333333;
  --muted:#777777;
  --paper:#ffffff;
  --mist:#f1f0ed;
  --stone:#e6e5e1;
  --line:#d8d6d1;
  --charcoal:#3a3a3a;
  --footer:#2a2a2a;
  --footer-deep:#1d1d1d;
  --kraft:#c9a77c;
  --blue:#3b5998;
  --sky:#2fa8e0;
  --red:#d63a2e;
}
*{box-sizing:border-box;margin:0;padding:0}
html,body{width:796px;height:1200px;overflow:hidden;background:var(--paper)}
body{font-family:"Open Sans",Arial,sans-serif;color:var(--ink)}
.page{position:relative;width:796px;height:1200px;overflow:hidden}
.abs{position:absolute}

/* top bar */
.topbar{top:0;left:0;width:796px;height:56px;background:var(--paper)}
.follow{left:40px;top:16px;font-size:9px;font-weight:600;letter-spacing:.5px;color:var(--muted)}
.social{left:122px;top:12px;display:flex;gap:5px}
.social span{width:15px;height:15px;border-radius:50%;display:block}
.phone{right:40px;top:13px;display:flex;align-items:center;gap:6px;color:var(--wine);font-weight:700;font-size:12px}
.phone i{width:16px;height:16px;border-radius:50%;background:var(--wine);display:flex;align-items:center;justify-content:center}

/* nav */
.nav{top:56px;left:0;width:796px;height:21px;background:var(--wine)}
.nav a{position:absolute;top:0;height:21px;line-height:21px;color:#fff;font-size:8.5px;font-weight:600;text-decoration:none;letter-spacing:.3px;padding:0 9px}
.nav a.active{background:var(--wine-dark)}
.brand{left:328px;top:0;width:140px;height:96px;background:var(--paper);border:1px solid var(--line);border-top:none;display:flex;align-items:center;justify-content:center;flex-direction:column;gap:6px;box-shadow:0 2px 4px rgba(0,0,0,.12)}
.brand-name{font-family:"Open Sans",Arial,sans-serif;font-weight:700;font-size:17px;color:var(--wine);letter-spacing:.2px}
.brand-mark{width:10px;height:10px;background:var(--wine)}

/* hero */
.hero{top:77px;left:0;width:796px;height:253px;background:linear-gradient(180deg,#f6f5f2,#ebe9e4)}
.hero-products{left:40px;top:30px;width:210px;height:200px;background:linear-gradient(90deg,#e9e3d6,#d9e4e2 55%,#e6e1d4);border-radius:4px}
.hero-copy{left:288px;top:70px;width:170px}
.hero-title{font-family:"Lobster",cursive;color:var(--wine);font-size:29px;line-height:1.1}
.hero-text{font-size:10px;color:var(--muted);line-height:1.4;margin-top:6px}
.btn-shop{display:inline-block;margin-top:12px;background:var(--wine);color:#fff;font-weight:700;font-size:11px;padding:6px 16px;border-radius:3px;letter-spacing:.5px}
.hero-portrait{left:470px;top:0;width:326px;height:253px;background:radial-gradient(ellipse at 45% 45%,#f1d6c6 0%,#e6c2ad 40%,#efe9e3 75%)}

/* about & services */
.info{top:330px;left:0;width:796px;height:232px;background:var(--stone)}
.heading{display:flex;align-items:center;justify-content:center;gap:10px;font-family:"Lobster",cursive;font-size:17px;color:var(--ink)}
.heading::before,.heading::after{content:"";height:1px;width:60px;background:#9a9a9a}
.about{left:40px;top:18px;width:350px}
.about p{margin-top:14px;font-size:9px;line-height:1.6;color:#666}
.about .more{display:block;margin-top:6px;font-size:9px;color:var(--wine);font-weight:600}
.services{left:420px;top:18px;width:336px}
.service-list{display:flex;justify-content:center;gap:60px;margin-top:28px}
.service{width:110px;text-align:center;font-size:9.5px;color:var(--ink)}
.service-icon{width:56px;height:56px;border-radius:50%;background:#4a4a4a;margin:0 auto 10px;display:flex;align-items:center;justify-content:center}

/* products */
.products{top:562px;left:0;width:796px;height:400px;background:var(--paper)}
.products .heading{position:absolute;top:16px;left:0;width:796px}
.card{width:163px;height:128px;border:1px solid var(--line);background:#fff;padding:8px}
.card h3{font-size:9.5px;font-weight:600;line-height:1.25;width:78px;color:var(--ink)}
.card-photo{position:absolute;right:8px;top:8px;width:66px;height:66px;border-radius:2px}
.card p{position:absolute;left:8px;top:82px;width:146px;font-size:7.5px;line-height:1.35;color:var(--muted)}
.btn-more{position:absolute;left:8px;bottom:8px;background:var(--wine);color:#fff;font-size:6.5px;font-weight:700;padding:3px 7px;letter-spacing:.3px}
.view-all{top:340px;left:0;width:796px;display:flex;align-items:center;justify-content:center;gap:10px}
.view-all::before,.view-all::after{content:"";width:50px;height:1px;background:var(--line)}
.view-all span{background:var(--charcoal);color:#fff;font-size:7px;font-weight:700;padding:3px 10px;letter-spacing:.5px}

/* promos */
.promo{top:930px;height:64px;width:230px;display:flex;align-items:center;justify-content:center;gap:14px;font-weight:700;font-size:11px;line-height:1.3;letter-spacing:.4px}
.promo.dark{background:var(--charcoal);color:#fff;outline:1px solid #555;outline-offset:-4px}
.promo.gift{background:var(--kraft);color:var(--wine);border:2px dashed var(--wine-dark);font-size:14px}

/* footer */
.footer{top:1012px;left:0;width:796px;height:166px;background:var(--footer)}
.footer h4{font-family:"Lobster",cursive;font-weight:400;color:#fff;font-size:14px;margin-bottom:10px}
.links{left:50px;top:18px}
.links li{list-style:none;font-size:8.5px;color:#bbb;margin-bottom:6px;padding-left:9px;position:relative}
.links li::before{content:"";position:absolute;left:0;top:4px;width:3px;height:3px;background:#bbb}
.store{left:295px;top:18px;width:220px}
.store .row{display:flex;gap:8px;font-size:8.5px;color:#bbb;line-height:1.45;margin-bottom:8px;align-items:flex-start}
.newsletter{left:535px;top:18px;width:221px}
.field{height:20px;background:#fff;border:1px solid #999;font-size:8px;color:#888;padding:0 7px;line-height:18px;margin-bottom:7px}
.btn-sub{display:inline-block;background:#555;color:#fff;font-size:8px;font-weight:700;padding:5px 14px;letter-spacing:.4px}
.bottombar{top:1178px;left:0;width:796px;height:22px;background:var(--footer-deep)}
.copy{left:40px;top:6px;font-size:7.5px;color:#999}
.bottom-social{right:40px;top:4px;display:flex;gap:4px}
.bottom-social span{width:13px;height:13px;border-radius:50%;border:1px solid #888;display:block}
</style>
</head>
<body>
<div class="page">

  <header class="topbar abs">
    <div class="follow abs">FOLLOW US ON</div>
    <div class="social abs">
      <span style="background:var(--blue)"></span>
      <span style="background:var(--sky)"></span>
      <span style="background:var(--blue)"></span>
      <span style="background:var(--red)"></span>
    </div>
    <div class="phone abs">
      <i><svg width="9" height="9" viewBox="0 0 24 24"><path fill="#fff" d="M6.6 10.8a15.1 15.1 0 0 0 6.6 6.6l2.2-2.2c.3-.3.7-.4 1-.2 1.1.4 2.3.6 3.6.6.6 0 1 .4 1 1V20c0 .6-.4 1-1 1C10.6 21 3 13.4 3 4c0-.6.4-1 1-1h3.5c.6 0 1 .4 1 1 0 1.3.2 2.5.6 3.6.1.3 0 .7-.2 1z"/></svg></i>
      123-456-7890
    </div>
  </header>

  <nav class="nav abs">
    <a class="active" style="left:40px">HOME</a>
    <a style="left:88px">LABORATORY</a>
    <a style="left:158px">PRODUCT LINES</a>
    <a style="left:492px">SERVICES</a>
    <a style="left:560px">NEWS</a>
    <a style="left:612px">SHOP</a>
    <a style="left:664px">CONTACT</a>
  </nav>

  <div class="brand abs">
    <span class="brand-mark"></span>
    <span class="brand-name">Casa Olmera</span>
  </div>

  <section class="hero abs">
    <div class="hero-products abs" role="img" aria-label="Frascos y botes de la línea familiar de cosmética natural"></div>
    <div class="hero-copy abs">
      <div class="hero-title">Linea Familiar</div>
      <p class="hero-text">Cuidado diario con aceites y extractos naturales para toda la familia.</p>
      <span class="btn-shop">SHOP NOW!</span>
    </div>
    <div class="hero-portrait abs" role="img" aria-label="Fotografía de una mujer sonriente con la piel cuidada"></div>
  </section>

  <section class="info abs">
    <div class="about abs">
      <h2 class="heading">About Casa Olmera</h2>
      <p>Desde hace generaciones elaboramos cosméticos como se hacía en las antiguas reboticas, con fórmulas sencillas y honestas. Seleccionamos plantas, aceites y extractos naturales de cultivo cercano para cuidar la piel de toda la familia. Cada producto nace en nuestro laboratorio con la paciencia del boticario y el rigor de la cosmética actual. Descubre nuestras líneas y encuentra la que mejor se adapta a ti.</p>
      <span class="more">Read More</span>
    </div>
    <div class="services abs">
      <h2 class="heading">Our Services</h2>
      <div class="service-list">
        <div class="service">
          <div class="service-icon"><svg width="26" height="26" viewBox="0 0 24 24"><circle cx="12" cy="8" r="4" fill="#fff"/><path d="M4 21c0-4.4 3.6-7 8-7s8 2.6 8 7z" fill="#fff"/></svg></div>
          Personalización
        </div>
        <div class="service">
          <div class="service-icon"><svg width="26" height="26" viewBox="0 0 24 24"><circle cx="12" cy="12" r="7" fill="none" stroke="#fff" stroke-width="3" stroke-dasharray="3 2"/><circle cx="12" cy="12" r="3" fill="#fff"/></svg></div>
          Fabricación A Terceros
        </div>
      </div>
    </div>
  </section>

  <section class="products abs">
    <h2 class="heading">Our Products</h2>

    <article class="card abs" style="left:40px;top:52px">
      <h3>Cuidados Naturales</h3>
      <div class="card-photo" role="img" aria-label="Caja y frasco de cuidados naturales" style="background:linear-gradient(135deg,#d8c3a0,#b59569)"></div>
      <p>Fórmulas suaves con ingredientes de origen natural.</p>
      <span class="btn-more">READ MORE</span>
    </article>
    <article class="card abs" style="left:224px;top:52px">
      <h3>Linea Recomendación Farmacéutica</h3>
      <div class="card-photo" role="img" aria-label="Frascos de la línea de recomendación farmacéutica" style="background:linear-gradient(135deg,#e4ddd0,#9b7a55)"></div>
      <p>Fórmulas suaves con ingredientes de origen natural.</p>
      <span class="btn-more">READ MORE</span>
    </article>
    <article class="card abs" style="left:408px;top:52px">
      <h3>Tratamiento Corporal</h3>
      <div class="card-photo" role="img" aria-label="Tubos y botes de tratamiento corporal" style="background:linear-gradient(135deg,#f0ece4,#cfc6b6)"></div>
      <p>Fórmulas suaves con ingredientes de origen natural.</p>
      <span class="btn-more">READ MORE</span>
    </article>
    <article class="card abs" style="left:592px;top:52px">
      <h3>Higiene Familiar</h3>
      <div class="card-photo" role="img" aria-label="Botes dosificadores de higiene familiar" style="background:linear-gradient(135deg,#eeeae2,#d6c7c0)"></div>
      <p>Fórmulas suaves con ingredientes de origen natural.</p>
      <span class="btn-more">READ MORE</span>
    </article>

    <article class="card abs" style="left:40px;top:196px">
      <h3>Cuidados Naturales</h3>
      <div class="card-photo" role="img" aria-label="Caja y frasco de aceite natural" style="background:linear-gradient(135deg,#dccaa8,#a98759)"></div>
      <p>Fórmulas suaves con ingredientes de origen natural.</p>
      <span class="btn-more">READ MORE</span>
    </article>
    <article class="card abs" style="left:224px;top:196px">
      <h3>Línea Aromática</h3>
      <div class="card-photo" role="img" aria-label="Pastillas de jabón aromático de colores" style="background:linear-gradient(135deg,#d9b6a4,#9fb08a 50%,#c9a6c2)"></div>
      <p>Fórmulas suaves con ingredientes de origen natural.</p>
      <span class="btn-more">READ MORE</span>
    </article>
    <article class="card abs" style="left:408px;top:196px">
      <h3>Cosmetics</h3>
      <div class="card-photo" role="img" aria-label="Frascos de cosmética facial" style="background:linear-gradient(135deg,#e7e3de,#7d6a66)"></div>
      <p>Fórmulas suaves con ingredientes de origen natural.</p>
      <span class="btn-more">READ MORE</span>
    </article>
    <article class="card abs" style="left:592px;top:196px">
      <h3>Línea Geriátrica</h3>
      <div class="card-photo" role="img" aria-label="Bote dosificador de la línea geriátrica" style="background:linear-gradient(135deg,#f2efe9,#d0d6cf)"></div>
      <p>Fórmulas suaves con ingredientes de origen natural.</p>
      <span class="btn-more">READ MORE</span>
    </article>

    <div class="view-all abs"><span>VIEW ALL</span></div>
  </section>

  <aside class="promo dark abs" style="left:40px">
    <svg width="34" height="22" viewBox="0 0 34 22"><rect x="1" y="3" width="20" height="13" fill="#fff"/><path d="M21 7h7l5 5v4H21z" fill="#fff"/><circle cx="8" cy="18" r="3" fill="#fff" stroke="#3a3a3a" stroke-width="1.5"/><circle cx="27" cy="18" r="3" fill="#fff" stroke="#3a3a3a" stroke-width="1.5"/></svg>
    <span>ENJOY EVERYDAY<br>FREE SHIPPING</span>
  </aside>
  <aside class="promo dark abs" style="left:283px">
    <svg width="24" height="26" viewBox="0 0 24 26"><rect x="3" y="1" width="18" height="24" fill="#fff"/><path d="M7 7h10M7 11h10M7 15h7" stroke="#3a3a3a" stroke-width="1.5"/></svg>
    <span>REQUEST A<br>FREE CATALOG</span>
  </aside>
  <aside class="promo gift abs" style="left:526px">
    <span>E-GIFT CARDS</span>
  </aside>

  <footer class="footer abs">
    <div class="links abs">
      <h4>Quick Links</h4>
      <ul>
        <li>Laboratorio</li>
        <li>Líneas de productos</li>
        <li>Servicios</li>
        <li>Noticias</li>
        <li>Comercio</li>
        <li>Tienda</li>
      </ul>
    </div>
    <div class="store abs">
      <h4>Store Information</h4>
      <div class="row">
        <svg width="10" height="13" viewBox="0 0 24 32"><path d="M12 0C5.4 0 0 5.4 0 12c0 9 12 20 12 20s12-11 12-20C24 5.4 18.6 0 12 0zm0 17a5 5 0 1 1 0-10 5 5 0 0 1 0 10z" fill="#bbb"/></svg>
        <span>C/ Mayor, 12, 37001<br>Salamanca, España</span>
      </div>
      <div class="row">
        <svg width="12" height="10" viewBox="0 0 24 18"><rect width="24" height="18" fill="#bbb"/><path d="M0 0l12 9 12-9" fill="none" stroke="#2a2a2a" stroke-width="2"/></svg>
        <span>info@casaolmera.es</span>
      </div>
      <div class="row">
        <svg width="11" height="11" viewBox="0 0 24 24"><path fill="#bbb" d="M6.6 10.8a15.1 15.1 0 0 0 6.6 6.6l2.2-2.2c.3-.3.7-.4 1-.2 1.1.4 2.3.6 3.6.6.6 0 1 .4 1 1V20c0 .6-.4 1-1 1C10.6 21 3 13.4 3 4c0-.6.4-1 1-1h3.5c.6 0 1 .4 1 1 0 1.3.2 2.5.6 3.6.1.3 0 .7-.2 1z"/></svg>
        <span style="font-size:11px;color:#ddd">+34 900 555 214</span>
      </div>
    </div>
    <div class="newsletter abs">
      <h4>Sign Up For Newsletter</h4>
      <div class="field">Correo Electrónico</div>
      <div class="field">Nombre del contacto</div>
      <span class="btn-sub">SUBSCRIBE</span>
    </div>
  </footer>

  <div class="bottombar abs">
    <div class="copy abs">© 2015 CasaOlmera.All Rights Reserved</div>
    <div class="bottom-social abs"><span></span><span></span><span></span><span></span></div>
  </div>

</div>
</body>
</html>
```